Design flyer for CLOM

Cedar Lamp Outreach Ministry (CLOM)
• The praise and worship team of RKTC
• The vision is to support members become the praise of God
• The mandate is to help members actualize the glorious privilege to be His praise
• Organize and coordinate Crosswind Friday Rally Night and Rivers of Gladness
• Goal is to enable members learn to worship God in spirit and in truth
• CLOM is made up of chapter praise team DRTSK praise team, the united Anthem Chorale and the Harmony Academy
• The goal is to manifest God’s glory as we worship Him in spirit and in truth

Join Cedar Lamp Outreach Ministry

```html
<!DOCTYPE html>
<html lang="en">
<head>
<meta charset="utf-8">
<title>Cedar Lamp Outreach Ministry – Flyer</title>
<link href="https://fonts.googleapis.com/css2?family=Alfa+Slab+One&family=Questrial&family=Nunito:wght@800&display=swap" rel="stylesheet">
<style>
  :root {
    --navy: #1d3a66;
    --green: #6aa23c;
    --green-light: #8cc152;
    --ink: #2a2a2a;
    --paper: #ffffff;
    --dusk-warm: #d9873a;
    --dusk-deep: #3a1a0c;
  }
  * { box-sizing: border-box; margin: 0; padding: 0; }
  html, body { width: 1200px; height: 1080px; overflow: hidden; background: var(--paper); }
  .flyer { position: relative; width: 1200px; height: 1080px; background: var(--paper); }

  .brand {
    position: absolute; top: 12px; left: 0; width: 1200px;
    display: flex; align-items: center; justify-content: center; gap: 18px;
  }
  .brand-mark { width: 108px; height: 108px; border-radius: 50%; background: var(--navy); flex: none; }
  .brand-name {
    font-family: "Questrial", sans-serif; font-size: 31px; color: var(--navy); white-space: nowrap;
  }

  .title {
    position: absolute; top: 146px; left: 0; width: 1200px; text-align: center;
    font-family: "Alfa Slab One", serif; font-size: 35px; letter-spacing: 7px;
    color: var(--navy); text-transform: uppercase; white-space: nowrap;
  }

  .points { position: absolute; top: 218px; left: 44px; width: 1140px; list-style: none; }
  .point {
    position: absolute; left: 0; display: flex; align-items: flex-start;
    font-family: "Questrial", sans-serif; font-size: 24px; line-height: 27px;
    color: var(--ink); letter-spacing: 3.6px; white-space: nowrap;
  }
  .point svg { flex: none; width: 36px; height: 36px; margin-top: -4px; margin-right: 50px; }
  .p1 { top: 4px; } .p2 { top: 56px; } .p3 { top: 104px; } .p4 { top: 170px; }
  .p5 { top: 236px; } .p6 { top: 284px; } .p7 { top: 348px; }

  .cta {
    position: absolute; top: 640px; left: 0; width: 1200px; text-align: center;
    font-family: "Nunito", sans-serif; font-weight: 800; font-size: 41px;
    letter-spacing: 3px; color: var(--green); white-space: nowrap;
  }

  .worship-photo {
    position: absolute; left: 0; top: 708px; width: 1200px; height: 372px;
    background: linear-gradient(180deg, var(--dusk-warm) 0%, var(--dusk-deep) 100%);
    -webkit-mask-image: linear-gradient(180deg, transparent 0%, #000 30%);
            mask-image: linear-gradient(180deg, transparent 0%, #000 30%);
  }
</style>
</head>
<body>
<main class="flyer">
  <header class="brand">
    <span class="brand-mark"></span>
    <span class="brand-name">Ridgekeep Tabernacle Collective</span>
  </header>

  <h1 class="title">Cedar Lamp Outreach Ministry (CLOM)</h1>

  <ul class="points">
    <li class="point p1"><svg viewBox="0 0 36 36"><circle cx="18" cy="18" r="16" fill="var(--navy)"/><circle cx="18" cy="18" r="11" fill="var(--green-light)"/><circle cx="18" cy="18" r="7" fill="#fff"/></svg><span>The praise and worship team of RKTC</span></li>
    <li class="point p2"><svg viewBox="0 0 36 36"><circle cx="18" cy="18" r="16" fill="var(--navy)"/><circle cx="18" cy="18" r="11" fill="var(--green-light)"/><circle cx="18" cy="18" r="7" fill="#fff"/></svg><span>The vision is to support members become the praise of God</span></li>
    <li class="point p3"><svg viewBox="0 0 36 36"><circle cx="18" cy="18" r="16" fill="var(--navy)"/><circle cx="18" cy="18" r="11" fill="var(--green-light)"/><circle cx="18" cy="18" r="7" fill="#fff"/></svg><span>The mandate is to help members actualize the glorious privilege<br>to be His praise</span></li>
    <li class="point p4"><svg viewBox="0 0 36 36"><circle cx="18" cy="18" r="16" fill="var(--navy)"/><circle cx="18" cy="18" r="11" fill="var(--green-light)"/><circle cx="18" cy="18" r="7" fill="#fff"/></svg><span>Organize and coordinate Crosswind Friday Rally Night and Rivers<br>of Gladness</span></li>
    <li class="point p5"><svg viewBox="0 0 36 36"><circle cx="18" cy="18" r="16" fill="var(--navy)"/><circle cx="18" cy="18" r="11" fill="var(--green-light)"/><circle cx="18" cy="18" r="7" fill="#fff"/></svg><span>Goal is to enable members learn to worship God in spirit and in truth</span></li>
    <li class="point p6"><svg viewBox="0 0 36 36"><circle cx="18" cy="18" r="16" fill="var(--navy)"/><circle cx="18" cy="18" r="11" fill="var(--green-light)"/><circle cx="18" cy="18" r="7" fill="#fff"/></svg><span>CLOM is made up of chapter praise team DRTSK praise team, the<br>united Anthem Chorale and the Harmony Academy</span></li>
    <li class="point p7"><svg viewBox="0 0 36 36"><circle cx="18" cy="18" r="16" fill="var(--navy)"/><circle cx="18" cy="18" r="11" fill="var(--green-light)"/><circle cx="18" cy="18" r="7" fill="#fff"/></svg><span>The goal is to manifest God’s glory as we worship Him in spirit<br>and in truth</span></li>
  </ul>

  <p class="cta">Join Cedar Lamp Outreach Ministry</p>

  <div class="worship-photo" role="img" aria-label="Photo placeholder: worshipper with raised arms against a sunset sky"></div>
</main>
</body>
</html>
```